Business card for acupunctist in Melbourne. Specialises in Fertility, pre and post natal care, pain

I am looking for a business card which is going to catch people eyes. Two sided, one side in a muted colour (keeping it feminine) (pink or yellow???)maybe with a little simple logo or picture, the other side I was thinking white with 3 colours (pink grey and yellow... Had these in mind.
Info on the card
Marla Quenby Acupuncture

Dr Marla Quenby (TCM Acupuncture)
Acupuncture for balancing body and mind.
Fernleaf Wellcraft
14 Corran Lane, Elsworth 3071.
94726150
0438219574
Marlatcm@quenbymail.com

Some other little logo/ designs I have liked are as follows:
http://www.dorisfelkaclinic.com/rates-and-insurance/
http://www.corinnetavish.com/
http://www.rz-needlework.co.uk/

Target Market(s)

professional women, people in pain, active people, people seeking a healthy lifefstyle.

Industry/Entity Type

Business

Font styles to use
Serif
Sans Serif

Colors
eea4c8
fde08a
aaaaaa

Requirements
Must have
• Must be eye catching, but not too loud and busy. Subltle is good. Simple is also good. The logo could be something that represents growth and health and nurturing. Again not too elaborate, very simple.
Thankyou
Should not have
• Electric colours, crazy fonts, Pictures of yin and yang, candles, or bodies.

```html
<!DOCTYPE html>
<html lang="en">
<head>
<meta charset="utf-8">
<title>Marla Quenby Acupuncture – Business Card</title>
<link rel="stylesheet" href="https://fonts.googleapis.com/css2?family=Libre+Baskerville&family=Open+Sans:wght@400;600&display=swap">
<style>
  :root {
    --pink: #eea4c8;
    --pink-deep: #e08fb8;
    --ink: #111111;
    --paper: #ffffff;
    --stage: #ececec;
    --serif: "Libre Baskerville", Georgia, serif;
    --sans: "Open Sans", Arial, sans-serif;
  }
  * { box-sizing: border-box; margin: 0; padding: 0; }
  html, body { width: 1200px; height: 945px; overflow: hidden; background: var(--stage); }
  .canvas { position: relative; width: 1200px; height: 945px; }
  .card {
    position: absolute; left: 220px; width: 760px; height: 434px;
    background: var(--paper); overflow: hidden;
    box-shadow: 0 4px 16px rgba(0,0,0,0.12);
  }
  .card--front { top: 22px; }
  .card--back { top: 489px; }
  .card__curve { position: absolute; inset: 0; width: 100%; height: 100%; }
  .card__curve path { fill: var(--pink); }

  .brand { position: absolute; display: flex; align-items: center; gap: 16px; }
  .brand__dot { border-radius: 50%; background: var(--pink); flex: none; }
  .brand__name { font-family: var(--serif); color: var(--pink-deep); line-height: 1.1; }
  .tagline {
    position: absolute; font-family: var(--sans); font-weight: 600;
    text-transform: uppercase; color: var(--ink); letter-spacing: 0.5px;
  }
  .practice-bar {
    position: absolute; background: var(--ink); color: var(--paper);
    font-family: var(--sans); padding: 3px 14px;
  }

  /* front */
  .card--front .brand { left: 60px; top: 110px; }
  .card--front .brand__dot { width: 58px; height: 58px; }
  .card--front .brand__name { font-size: 42px; }
  .card--front .tagline { left: 60px; top: 240px; font-size: 15px; }
  .card--front .practice-bar { left: 400px; top: 270px; font-size: 16px; }

  /* back */
  .practitioner { position: absolute; right: 70px; top: 52px; text-align: right; }
  .practitioner__name { font-family: var(--serif); font-size: 32px; color: var(--ink); text-transform: uppercase; letter-spacing: 1px; }
  .practitioner__title { font-family: var(--serif); font-size: 12px; color: var(--ink); margin-top: 2px; margin-right: 60px; }

  .card--back .brand { left: 40px; top: 236px; gap: 10px; }
  .card--back .brand__dot { width: 30px; height: 30px; }
  .card--back .brand__name { font-size: 20px; }
  .card--back .tagline { left: 40px; top: 300px; font-size: 9px; }
  .card--back .practice-bar { left: 130px; top: 318px; font-size: 10px; padding: 1px 10px; }

  .contact-bar {
    position: absolute; right: 58px; height: 30px; background: var(--ink); color: var(--paper);
    font-family: var(--sans); font-size: 15px; letter-spacing: 1px; text-transform: uppercase;
    display: flex; align-items: center; justify-content: flex-end; padding: 0 22px 0 16px;
  }
  .contact-bar--email { top: 150px; width: 330px; }
  .contact-bar--address { top: 194px; width: 400px; }
  .icon { position: absolute; width: 40px; height: 40px; right: 30px; }
  .icon--email { top: 145px; }
  .icon--home { top: 189px; }
  .icon--phone { top: 270px; width: 46px; height: 46px; right: 24px; }
  .phones { position: absolute; right: 84px; top: 236px; text-align: right; font-family: var(--sans); color: var(--ink); font-size: 46px; line-height: 1.05; letter-spacing: 1px; }
</style>
</head>
<body>
<main class="canvas">

  <section class="card card--front" aria-label="Card front">
    <svg class="card__curve" viewBox="0 0 760 434" preserveAspectRatio="none" aria-hidden="true">
      <path d="M250 434 C 420 300, 560 170, 760 90 L760 434 Z"/>
    </svg>
    <div class="brand">
      <span class="brand__dot"></span>
      <span class="brand__name">Marla Quenby<br>Acupuncture</span>
    </div>
    <p class="tagline">Acupuncture for balancing body and mind.</p>
    <p class="practice-bar">“Fernleaf Wellcraft”</p>
  </section>

  <section class="card card--back" aria-label="Card back">
    <svg class="card__curve" viewBox="0 0 760 434" preserveAspectRatio="none" aria-hidden="true">
      <path d="M0 434 C 220 300, 430 130, 760 100 L760 434 Z"/>
    </svg>

    <header class="practitioner">
      <h1 class="practitioner__name">Dr Marla Quenby</h1>
      <p class="practitioner__title">(TCM ACUPUNCTURE)</p>
    </header>

    <p class="contact-bar contact-bar--email">Marlatcm@quenbymail.com</p>
    <svg class="icon icon--email" viewBox="0 0 40 40" aria-label="Email">
      <circle cx="20" cy="20" r="19" fill="#111"/>
      <rect x="10" y="13" width="20" height="14" fill="none" stroke="#fff" stroke-width="2"/>
      <path d="M10 13 L20 21 L30 13" fill="none" stroke="#fff" stroke-width="2"/>
    </svg>

    <p class="contact-bar contact-bar--address">14 Corran Lane, Elsworth 3071.</p>
    <svg class="icon icon--home" viewBox="0 0 40 40" aria-label="Address">
      <circle cx="20" cy="20" r="19" fill="#111"/>
      <path d="M9 21 L20 11 L31 21 L28 21 L28 30 L12 30 L12 21 Z" fill="#fff"/>
    </svg>

    <p class="phones">94726150<br>0438219574</p>
    <svg class="icon icon--phone" viewBox="0 0 46 46" aria-label="Phone">
      <circle cx="23" cy="23" r="22" fill="#111"/>
      <path d="M15 12 C13 14 13 19 17 25 C21 31 27 35 31 34 L34 31 L29 26 L26 28 C23 27 19 23 18 20 L20 17 L16 12 Z" fill="#fff"/>
    </svg>

    <div class="brand">
      <span class="brand__dot"></span>
      <span class="brand__name">Marla Quenby<br>Acupuncture</span>
    </div>
    <p class="tagline">Acupuncture for balancing body and mind.</p>
    <p class="practice-bar">“Fernleaf Wellcraft”</p>
  </section>

</main>
</body>
</html>
```